New Infusion Pharmacy needs Business Card design

Hello!

We are Verant Infusion Pharmacy, are we are looking for a two sided, clean and modern business card.

First, let me give you a little bit about what an infusion pharmacy does...
We compound and fill prescriptions for drugs that are injectable, meaning that they are administered via an IV bag or a syringe. Basically anything that is too advanced for a normal pill pharmacy to fill. We compound everything in our state of the art clean room, then deliver it directly to the patients home. We have an outside sales force that markets to hospitals, home health agencies, and doctor's offices.

as for the business card...
We are looking for a clean, modern card. our colors are in our logo, kind of a light bule and a darker blue. We do really like the rounded corners on the card. Also, we would like the back of the card to be the reverse colors of the front, for example, if the front of the card has a light background, then the back of the card will have a dark background.

On the back side of the card we want to have our logo, then list some of the services we offer:
-IVIG
-TPN
-Enteral Nutrition
-IV Antibiotics
-IV Hydration
-Blood Factors
-Chemotherapy
-Pain Management

Our logo is uploaded in .psd format, if you need a different format let me know and i'll throw it up here.

Thank you so much!!

Industry/Entity Type

Pharmacy

Requirements
Must have
• Front of Card: (no particular order, please arrange in whatever way you think looks best!)
-Employee Name
-Title
-Office Phone #
-Cell Phone #
-Fax #
-email address - marlo@verantcareinfuse.com
-office address - 4127 Delmore St. Larkview, CA 93418
-Web Site - www.verantcareinfuse.com

```html
<!DOCTYPE html>
<html lang="en">
<head>
<meta charset="utf-8">
<title>Verant Infusion Pharmacy – Business Card</title>
<link rel="stylesheet" href="https://fonts.googleapis.com/css2?family=Montserrat:wght@400;600;700&family=Questrial&display=swap">
<style>
  :root {
    --backdrop: #8e8e8e;
    --card-light: #f3f4f5;
    --navy: #1b5670;
    --teal: #2a9dbf;
    --ink: #3a3f44;
    --muted: #6b7278;
    --ghost: #b6ccd6;
    --grad-light: #45b7cf;
    --grad-mid: #2a93bd;
    --grad-dark: #1d4a8a;
    --white: #ffffff;
  }
  * { box-sizing: border-box; margin: 0; padding: 0; }
  html, body {
    width: 1200px; height: 840px; overflow: hidden;
    background: var(--backdrop);
  }
  .stage {
    width: 1200px; height: 840px;
    display: flex; align-items: center; justify-content: center; gap: 40px;
  }
  .card {
    position: relative;
    width: 520px; height: 297px;
    border-radius: 12px;
    overflow: hidden;
    box-shadow: 0 6px 18px rgba(0,0,0,0.25);
  }

  /* Front */
  .card-front {
    background: var(--card-light);
    padding: 30px 34px;
    font-family: "Questrial", sans-serif;
    color: var(--ink);
  }
  .brand { font-family: "Montserrat", sans-serif; font-weight: 600; line-height: 1; }
  .card-front .brand { color: var(--navy); }
  .brand-name { display: block; font-size: 40px; letter-spacing: 2px; }
  .brand-tag { display: block; font-size: 10.5px; letter-spacing: 6.2px; margin-top: 4px; }
  .person { margin-top: 22px; }
  .person-name {
    font-family: "Montserrat", sans-serif; font-weight: 700;
    font-size: 15px; color: var(--navy); letter-spacing: 0.5px;
  }
  .person-title { font-size: 11.5px; color: var(--muted); margin-top: 1px; }
  .contact { margin-top: 8px; font-size: 12px; line-height: 1.45; }
  .contact-label {
    font-family: "Montserrat", sans-serif; font-weight: 700;
    font-size: 11.5px; color: var(--teal);
  }
  .office { margin-top: 14px; font-size: 12px; line-height: 1.45; }
  .office .contact-label { color: var(--navy); }
  .spacer { display: inline-block; width: 10px; }
  .ghost-name {
    position: absolute; right: 6px; top: 0; bottom: 0;
    writing-mode: vertical-rl; transform: rotate(180deg);
    font-family: "Montserrat", sans-serif; font-weight: 600;
    font-size: 64px; letter-spacing: 4px; color: var(--ghost);
    text-align: center; line-height: 1;
  }

  /* Back */
  .card-back {
    background: linear-gradient(30deg, var(--grad-light) 0%, var(--grad-mid) 45%, var(--grad-dark) 100%);
    color: var(--white);
    text-align: center;
  }
  .back-curves { position: absolute; inset: 0; }
  .back-content {
    position: relative;
    display: flex; flex-direction: column; align-items: center;
    padding-top: 62px;
  }
  .card-back .brand { color: var(--white); }
  .card-back .brand-name { font-size: 50px; letter-spacing: 2px; }
  .card-back .brand-tag { font-size: 12px; letter-spacing: 7px; margin-top: 5px; }
  .services {
    list-style: none; margin-top: 38px;
    font-family: "Questrial", sans-serif; font-size: 15px; line-height: 1.45;
  }
</style>
</head>
<body>
<main class="stage">
  <section class="card card-front" aria-label="Card front">
    <div class="brand">
      <span class="brand-name">VERANT</span>
      <span class="brand-tag">INFUSION PHARMACY</span>
    </div>
    <div class="person">
      <p class="person-name">MARLO PENNINGTON</p>
      <p class="person-title">Chief Manager</p>
    </div>
    <div class="contact">
      <p><span class="contact-label">Cell:</span> (555) 310-0148</p>
      <p><span class="contact-label">Email:</span> marlo@verantcareinfuse.com</p>
    </div>
    <div class="office">
      <p>4127 Delmore St., Larkview, CA 93418</p>
      <p><span class="contact-label">Phone:</span> (555) 310-0172<span class="spacer"></span><span class="contact-label">Fax:</span> (555) 310-0193</p>
      <p>www.verantcareinfuse.com</p>
    </div>
    <div class="ghost-name" aria-hidden="true">VERANT</div>
  </section>

  <section class="card card-back" aria-label="Card back">
    <svg class="back-curves" viewBox="0 0 520 297" preserveAspectRatio="none" aria-hidden="true">
      <path d="M0 150 Q260 60 520 120 L520 297 L0 297 Z" fill="#ffffff" fill-opacity="0.12"/>
      <path d="M0 250 Q260 150 520 230 L520 297 L0 297 Z" fill="#ffffff" fill-opacity="0.08"/>
    </svg>
    <div class="back-content">
      <div class="brand">
        <span class="brand-name">VERANT</span>
        <span class="brand-tag">INFUSION PHARMACY</span>
      </div>
      <ul class="services">
        <li>Enteral Nutrition • IV Antibiotics</li>
        <li>Pain Management • IVIG • TPN • IV Hydration</li>
        <li>Blood Factors • Chemotherapy</li>
      </ul>
    </div>
  </section>
</main>
</body>
</html>
```